Design mobile friendly review and ranking site

We're working on a corporate website for reviewing and ranking fellow employees. We need the website to look both fun and professional and it needs to be responsive - to it works on mobile and desktop.

Looking for css and HTML for 3 key pages as well as a header and footer for the site. Also would need any supporting graphics as part of the design.

Target Market(s)

Professionals in their 20s, 30s, and 40s.

Industry/Entity Type

Internet

Coding

Coded - Design and coding required

Number of Pages Required

3 page

Font styles to use
Sans Serif

Requirements
Must have
• 3 key pages we need (note included screenshots for each - these are just super rough cuts so you see examples of the content.)
• a) main-intro: A compelling into page with a login/registration form. Should be sleek/modern/enticing. Also we would show the ranking for the top 3 people to tease people re: content.
• b) main-page: Has two sections: One at the top where you would rate someone and one at the bottom where it shows a ranking of people.
• c) profile page: This is where you view a specific person. You see the person's picture, some info about the person, you see their overall rating, you can rate them, and you also see their historical ratings.
Nice to have
• Note we need css and HTML for this. It should feel as sleek and modern. Note also must be responsive design so it works well in mobile and desktop.

```html
<!DOCTYPE html>
<html lang="en">
<head>
<meta charset="utf-8">
<title>Crew Rankings – Rate</title>
<link href="https://fonts.googleapis.com/css2?family=Raleway:wght@400;500;600;700&display=swap" rel="stylesheet">
<style>
:root{
  --orange:#ff9800;
  --black:#000;
  --dark:#1c1c1c;
  --ink:#222;
  --muted:#555;
  --line:#cfcfcf;
  --white:#fff;
}
*{box-sizing:border-box;margin:0;padding:0}
html,body{width:1200px;height:959px;overflow:hidden}
body{font-family:'Raleway',sans-serif;color:var(--ink);position:relative;background:#e9e6de}
.abs{position:absolute}
.backdrop{position:absolute;left:0;top:86px;width:1200px;height:821px;
  background:radial-gradient(ellipse at 60% 45%,#f4f1e6 0%,#ddd8cc 45%,#b9b8b8 80%,#a9aab0 100%)}
.site-header{position:absolute;left:0;top:0;width:1200px;height:86px;background:var(--black);border-bottom:2px solid var(--orange)}
.brand{position:absolute;left:99px;top:22px;color:var(--orange);font-weight:500;font-size:24px;letter-spacing:4px;line-height:1}
.level{position:absolute;left:620px;top:36px;color:var(--white);font-weight:700;font-size:14px}
.btn-profile{position:absolute;left:821px;top:27px;width:158px;height:34px;background:var(--orange);color:var(--white);font-weight:700;font-size:13px;display:flex;align-items:center;justify-content:center;gap:8px}
.btn-logout{position:absolute;left:992px;top:27px;width:108px;height:34px;border:1px solid var(--white);color:var(--white);font-weight:700;font-size:13px;display:flex;align-items:center;justify-content:center;gap:9px}
.page-title{position:absolute;left:0;width:1200px;top:126px;text-align:center;font-size:24px;font-weight:400;color:#111}
.rate-panel{position:absolute;left:98px;top:177px;width:1002px;height:281px;background:rgba(255,255,255,.97)}
.photo{background:linear-gradient(160deg,#9a8a7c,#5b4a40 55%,#2e3c5a);border:3px solid #fff;outline:1px solid #ddd}
.card-photo{border:3px solid #fff;outline:2px solid #111;background:linear-gradient(160deg,#b8b8b8,#6f6f6f 55%,#3a3f55)}
.label{font-size:14px;color:var(--muted)}
.name{font-weight:600;font-size:15px;color:#222;text-align:center}
.btn-outline{border:1px solid #222;background:#fff;display:flex;align-items:center;justify-content:center;font-size:13px;color:#222}
.comment{position:absolute;left:539px;top:203px;width:529px;height:71px;border:1px solid var(--line);background:#fff;padding:9px 10px;font-size:12px;color:#444}
.btn-solid{position:absolute;height:34px;width:118px;display:flex;align-items:center;justify-content:center;color:#fff;font-weight:700;font-size:12px}
.filter-bar{position:absolute;left:118px;top:364px;width:948px;height:66px;background:var(--dark)}
.filter-best{position:absolute;left:20px;top:17px;width:121px;height:35px;background:var(--orange);color:#fff;font-weight:600;font-size:14px;display:flex;align-items:center;justify-content:center}
.filter-word{position:absolute;top:26px;color:#fff;font-weight:700;font-size:14px}
.select{position:absolute;top:17px;height:35px;background:#fff;font-size:13px;color:#333;padding-left:19px;display:flex;align-items:center}
.select svg{position:absolute;right:14px;top:13px}
.rank{font-weight:700;font-size:12px;color:#222}
.info{font-size:13px;color:#333}
.divider{position:absolute;left:98px;top:686px;width:1004px;height:1px;background:#d8d4cc}
.site-footer{position:absolute;left:0;top:907px;width:1200px;height:52px;background:var(--dark)}
.copy{position:absolute;left:99px;top:20px;color:#ddd;font-size:12px}
.social{position:absolute;top:13px;width:28px;height:28px;border-radius:50%;background:#bdbdbd}
.stars{position:absolute}
</style>
</head>
<body>
<svg width="0" height="0" style="position:absolute">
  <defs>
    <symbol id="star" viewBox="0 0 24 24"><path d="M12 2l2.9 6.6 7.1.6-5.4 4.7 1.6 7-6.2-3.7-6.2 3.7 1.6-7L2 9.2l7.1-.6z"/></symbol>
  </defs>
</svg>

<div class="backdrop" role="img" aria-label="Soft blurred photo of colleagues in an office"></div>

<header class="site-header">
  <div class="brand">CREW RANKINGS</div>
  <div class="level">Level 3 - 41 Point to level 4</div>
  <div class="btn-profile">
    <svg width="13" height="14" viewBox="0 0 13 14" fill="#fff"><circle cx="6.5" cy="4" r="3.5"/><path d="M0 14c0-4 3-6 6.5-6S13 10 13 14z"/></svg>
    YOUR PROFILE
    <svg width="11" height="7" viewBox="0 0 11 7"><path d="M1 1l4.5 4.5L10 1" stroke="#fff" stroke-width="1.6" fill="none"/></svg>
  </div>
  <div class="btn-logout">
    <svg width="12" height="14" viewBox="0 0 12 14" fill="#fff"><path d="M3 6V4a3 3 0 016 0v2h-1.5V4a1.5 1.5 0 00-3 0v2z"/><rect x="0" y="6" width="12" height="8" rx="1"/></svg>
    LOGOUT
  </div>
</header>

<h1 class="page-title">Anonymously Rate This Person For A Point</h1>

<section class="rate-panel">
  <div class="photo abs" style="left:21px;top:21px;width:112px;height:91px" role="img" aria-label="Portrait photo of Daniel"></div>
  <div class="name abs" style="left:21px;top:126px;width:112px">Daniel</div>

  <div class="label abs" style="left:152px;top:24px">Smart</div>
  <div class="label abs" style="left:152px;top:54px">Average Personality</div>
  <div class="label abs" style="left:152px;top:85px">Works crazy hard</div>

  <svg class="stars" style="left:302px;top:25px" width="76" height="13" viewBox="0 0 76 13" fill="var(--orange)" stroke="var(--orange)" stroke-width="2">
    <use href="#star" x="0" width="13" height="13"/><use href="#star" x="15.5" width="13" height="13"/><use href="#star" x="31" width="13" height="13"/><use href="#star" x="46.5" width="13" height="13"/><use href="#star" x="62" width="13" height="13" fill="none"/>
  </svg>
  <svg class="stars" style="left:302px;top:56px" width="76" height="13" viewBox="0 0 76 13" fill="var(--orange)" stroke="var(--orange)" stroke-width="2">
    <use href="#star" x="0" width="13" height="13"/><use href="#star" x="15.5" width="13" height="13"/><use href="#star" x="31" width="13" height="13"/><use href="#star" x="46.5" width="13" height="13" fill="none"/><use href="#star" x="62" width="13" height="13" fill="none"/>
  </svg>
  <svg class="stars" style="left:302px;top:87px" width="76" height="13" viewBox="0 0 76 13" fill="var(--orange)" stroke="var(--orange)" stroke-width="2">
    <use href="#star" x="0" width="13" height="13"/><use href="#star" x="15.5" width="13" height="13"/><use href="#star" x="31" width="13" height="13"/><use href="#star" x="46.5" width="13" height="13"/><use href="#star" x="62" width="13" height="13"/>
  </svg>

  <div class="btn-outline abs" style="left:151px;top:118px;width:225px;height:33px;font-weight:600;font-size:14px">View Reviews</div>

  <div class="comment" style="left:441px;top:26px">(Optional) Write an anonymous comment above this person.</div>
  <div class="btn-solid" style="left:441px;top:117px;background:var(--orange)">SKIP</div>
  <div class="btn-solid" style="left:571px;top:117px;background:var(--black)">SAVE</div>

  <div class="filter-bar" style="left:20px;top:187px">
    <div class="filter-best">Best</div>
    <div class="filter-word" style="left:155px">in</div>
    <div class="select" style="left:190px;width:326px">All Function
      <svg width="11" height="7" viewBox="0 0 11 7"><path d="M1 1l4.5 4.5L10 1" stroke="#222" stroke-width="1.6" fill="none"/></svg></div>
    <div class="filter-word" style="left:539px">and</div>
    <div class="select" style="left:588px;width:341px">All Levels
      <svg width="11" height="7" viewBox="0 0 11 7"><path d="M1 1l4.5 4.5L10 1" stroke="#222" stroke-width="1.6" fill="none"/></svg></div>
  </div>
</section>

<!-- ranking cards -->
<div class="rank abs" style="left:110px;top:551px">#1 BEST</div>
<div class="card-photo abs" style="left:173px;top:511px;width:136px;height:106px" role="img" aria-label="Portrait photo of Sam Porter"></div>
<div class="name abs" style="left:171px;top:635px;width:140px">Sam Porter</div>
<div class="info abs" style="left:338px;top:508px;line-height:23.5px">Point : 4.1<br>Number of reviews : 5<br>Smart<br>Easy to work with<br>Hard worker</div>
<svg class="stars" style="left:469px;top:559px" width="86" height="59" viewBox="0 0 86 59" fill="var(--orange)" stroke="var(--orange)" stroke-width="2">
  <g><use href="#star" x="0" width="12" height="12"/><use href="#star" x="18" width="12" height="12"/><use href="#star" x="36" width="12" height="12"/><use href="#star" x="54" width="12" height="12" fill="none"/><use href="#star" x="72" width="12" height="12" fill="none"/></g>
  <g transform="translate(0,23)"><use href="#star" x="0" width="12" height="12"/><use href="#star" x="18" width="12" height="12"/><use href="#star" x="36" width="12" height="12"/><use href="#star" x="54" width="12" height="12" fill="none"/><use href="#star" x="72" width="12" height="12" fill="none"/></g>
  <g transform="translate(0,45)"><use href="#star" x="0" width="12" height="12"/><use href="#star" x="18" width="12" height="12"/><use href="#star" x="36" width="12" height="12"/><use href="#star" x="54" width="12" height="12" fill="none"/><use href="#star" x="72" width="12" height="12" fill="none"/></g>
</svg>
<div class="btn-outline abs" style="left:340px;top:629px;width:106px;height:29px">View Detail</div>

<div class="rank abs" style="left:651px;top:551px">#2 BEST</div>
<div class="card-photo abs" style="left:719px;top:510px;width:136px;height:106px" role="img" aria-label="Portrait photo of Daniel"></div>
<div class="name abs" style="left:717px;top:633px;width:140px">Daniel</div>
<div class="info abs" style="left:881px;top:507px;line-height:20.5px">Point : 4.1<br>Number of reviews : 5<br>Smart<br>Easy to work with<br>Hard worker</div>
<svg class="stars" style="left:1014px;top:556px" width="86" height="50" viewBox="0 0 86 50" fill="var(--orange)" stroke="var(--orange)" stroke-width="2">
  <g><use href="#star" x="0" width="12" height="12"/><use href="#star" x="18" width="12" height="12"/><use href="#star" x="36" width="12" height="12"/><use href="#star" x="54" width="12" height="12" fill="none"/><use href="#star" x="72" width="12" height="12" fill="none"/></g>
  <g transform="translate(0,18)"><use href="#star" x="0" width="12" height="12"/><use href="#star" x="18" width="12" height="12"/><use href="#star" x="36" width="12" height="12"/><use href="#star" x="54" width="12" height="12" fill="none"/><use href="#star" x="72" width="12" height="12" fill="none"/></g>
  <g transform="translate(0,35)"><use href="#star" x="0" width="12" height="12"/><use href="#star" x="18" width="12" height="12"/><use href="#star" x="36" width="12" height="12"/><use href="#star" x="54" width="12" height="12" fill="none"/><use href="#star" x="72" width="12" height="12" fill="none"/></g>
</svg>
<div class="btn-outline abs" style="left:880px;top:629px;width:114px;height:29px">View Detail</div>

<div class="divider"></div>

<div class="rank abs" style="left:101px;top:763px">#3 BEST</div>
<div class="card-photo abs" style="left:173px;top:717px;width:136px;height:106px" role="img" aria-label="Portrait photo of Sam Porter"></div>
<div class="name abs" style="left:168px;top:836px;width:140px">Sam Porter</div>
<div class="info abs" style="left:338px;top:713px;line-height:20px">Point : 4.1<br>Number of reviews : 5<br>Smart<br>Easy to work with<br>Hard worker</div>
<svg class="stars" style="left:468px;top:763px" width="86" height="50" viewBox="0 0 86 50" fill="var(--orange)" stroke="var(--orange)" stroke-width="2">
  <g><use href="#star" x="0" width="12" height="12"/><use href="#star" x="18" width="12" height="12"/><use href="#star" x="36" width="12" height="12"/><use href="#star" x="54" width="12" height="12" fill="none"/><use href="#star" x="72" width="12" height="12" fill="none"/></g>
  <g transform="translate(0,18)"><use href="#star" x="0" width="12" height="12"/><use href="#star" x="18" width="12" height="12"/><use href="#star" x="36" width="12" height="12"/><use href="#star" x="54" width="12" height="12" fill="none"/><use href="#star" x="72" width="12" height="12" fill="none"/></g>
  <g transform="translate(0,36)"><use href="#star" x="0" width="12" height="12"/><use href="#star" x="18" width="12" height="12"/><use href="#star" x="36" width="12" height="12"/><use href="#star" x="54" width="12" height="12" fill="none"/><use href="#star" x="72" width="12" height="12" fill="none"/></g>
</svg>
<div class="btn-outline abs" style="left:340px;top:830px;width:114px;height:29px">View Detail</div>

<div class="rank abs" style="left:647px;top:759px">#4 BEST</div>
<div class="card-photo abs" style="left:719px;top:716px;width:136px;height:106px" role="img" aria-label="Portrait photo of Sam Porter"></div>
<div class="name abs" style="left:720px;top:836px;width:140px">Sam Porter</div>
<div class="info abs" style="left:880px;top:712px;line-height:20px">Point : 4.1<br>Number of reviews : 5<br>Smart<br>Easy to work with<br>Hard worker</div>
<svg class="stars" style="left:1014px;top:762px" width="86" height="50" viewBox="0 0 86 50" fill="var(--orange)" stroke="var(--orange)" stroke-width="2">
  <g><use href="#star" x="0" width="12" height="12"/><use href="#star" x="18" width="12" height="12"/><use href="#star" x="36" width="12" height="12"/><use href="#star" x="54" width="12" height="12" fill="none"/><use href="#star" x="72" width="12" height="12" fill="none"/></g>
  <g transform="translate(0,18)"><use href="#star" x="0" width="12" height="12"/><use href="#star" x="18" width="12" height="12"/><use href="#star" x="36" width="12" height="12"/><use href="#star" x="54" width="12" height="12" fill="none"/><use href="#star" x="72" width="12" height="12" fill="none"/></g>
  <g transform="translate(0,35)"><use href="#star" x="0" width="12" height="12"/><use href="#star" x="18" width="12" height="12"/><use href="#star" x="36" width="12" height="12"/><use href="#star" x="54" width="12" height="12" fill="none"/><use href="#star" x="72" width="12" height="12" fill="none"/></g>
</svg>
<div class="btn-outline abs" style="left:880px;top:831px;width:114px;height:29px">View Detail</div>

<footer class="site-footer">
  <div class="copy">© 2016 Crewrankings. All Rights Reserved.</div>
  <div class="social" style="left:971px"></div>
  <div class="social" style="left:1005px"></div>
  <div class="social" style="left:1039px"></div>
  <div class="social" style="left:1074px"></div>
</footer>
</body>
</html>
```